Local water manufacturing needs a re-design to an existing label design.

We need to change an existing label design for an established water manufacturing company located in the Bahamas. We are expanding into a new 1.5L size product and would like to do so with an updated label design that incorporates an animated pink conch shell (sample included) with at least one other bright color to match the existing blue background and the pink conch shell. The final design should convey an island feel and vibe. The existing label is only a suggestion. The entire label can be completely changed.

Target Market(s)

Hotels, tourist

Industry/Entity Type

Water Manufacturing

Requirements
Must have
• Bright color that matches blue cap and pink conch shell
Nice to have
• Simple design with sleek modern look.

```html
<!DOCTYPE html>
<html lang="en">
<head>
<meta charset="utf-8">
<title>Coralis Filtered Water – 1.5 Liter Label</title>
<link href="https://fonts.googleapis.com/css2?family=Fira+Sans:wght@300;400;500;600&display=swap" rel="stylesheet">
<style>
  :root {
    --page-bg: #e7e8ea;
    --ocean-blue: #1b5dab;
    --conch-pink: #e8687e;
    --white: #ffffff;
    --sky-top: #e9f1f6;
    --sky-mid: #b9d3df;
    --hills: #5f9aa3;
    --forest: #2f6f68;
  }
  * { margin: 0; padding: 0; box-sizing: border-box; }
  html, body { width: 1200px; height: 1200px; overflow: hidden; }
  body {
    background: var(--page-bg);
    font-family: "Fira Sans", sans-serif;
    position: relative;
  }

  .label {
    position: absolute;
    width: 496px;
    height: 396px;
    border-radius: 16px;
    overflow: hidden;
    background: var(--conch-pink);
    box-shadow: 3px 4px 6px rgba(0,0,0,0.18);
  }
  .label--front { left: 352px; top: 118px; }
  .label--wrapped { left: 352px; top: 636px; transform: rotate(-90deg); }

  .brand-band {
    position: absolute; left: 0; top: 0; width: 100%; height: 129px;
    background: var(--ocean-blue);
  }
  .landscape {
    position: absolute; left: 0; top: 129px; width: 100%; height: 180px;
    background: linear-gradient(180deg, var(--sky-top) 0%, var(--sky-mid) 35%, var(--hills) 62%, var(--forest) 100%);
  }
  .volume {
    position: absolute; left: 12px; top: 12px;
    color: var(--white); font-size: 11px; font-weight: 500;
    writing-mode: vertical-rl;
  }
  .conch-art {
    position: absolute; left: 19px; top: 11px; width: 140px; height: 232px;
    border-radius: 60px 60px 50px 70px;
    background: linear-gradient(180deg, rgba(255,255,255,0.18) 0%, rgba(255,255,255,0.12) 45%, rgba(232,104,126,0.35) 60%, rgba(232,104,126,0.25) 100%);
  }
  .brand-name {
    position: absolute; left: 160px; top: 16px;
    color: var(--white); font-size: 86px; font-weight: 600; line-height: 1;
    letter-spacing: 0.5px;
  }
  .product-name {
    position: absolute; right: 33px; top: 140px;
    color: var(--ocean-blue); font-size: 27px; font-weight: 600; line-height: 1;
  }
  .product-note {
    position: absolute; left: 254px; top: 173px;
    color: var(--conch-pink); font-size: 14.5px; font-weight: 400; letter-spacing: 0.3px;
  }
  .recycle-icon { position: absolute; left: 46px; top: 268px; width: 34px; height: 34px; }
  .wave { position: absolute; left: 0; top: 0; width: 496px; height: 396px; }

  .nutrition {
    position: absolute; left: 19px; top: 312px; width: 242px; height: 73px;
    background: var(--white); border: 1.2px solid var(--ocean-blue);
    color: var(--ocean-blue); font-size: 6.4px; line-height: 1.1;
    padding: 2px 3px;
  }
  .nutrition__title { position: absolute; left: 5px; top: 2px; font-size: 10px; font-weight: 600; line-height: 1.05; }
  .nutrition__serving { position: absolute; left: 5px; top: 26px; width: 58px; }
  .nutrition__calories {
    position: absolute; left: 5px; top: 54px; width: 58px;
    border-top: 1px solid var(--ocean-blue); padding-top: 2px;
  }
  .nutrition__calories b { position: absolute; right: 8px; top: 3px; font-size: 9px; font-weight: 400; }
  .nutrition__col { position: absolute; top: 2px; width: 84px; }
  .nutrition__col--a { left: 65px; }
  .nutrition__col--b { left: 154px; }
  .nutrition__row {
    display: flex; justify-content: space-between;
    height: 9.4px; border-bottom: 1.6px solid var(--ocean-blue);
  }
  .nutrition__row--head { font-weight: 500; border-bottom-width: 2px; height: 9px; margin-bottom: 1px; }
  .nutrition__row--plain { border-bottom-width: 0; }
  .nutrition__foot { position: absolute; left: 65px; top: 63px; font-size: 5.4px; }

  .bottler {
    position: absolute; left: 264px; top: 317px;
    color: var(--white); font-size: 6.4px; line-height: 1.35;
  }
  .bottler b { font-weight: 600; }
  .bottler p + p { margin-top: 6px; }
</style>
</head>
<body>

<div class="label label--front">
  <div class="brand-band"></div>
  <div class="landscape" role="img" aria-label="Photograph of misty green hills around a calm island lagoon"></div>
  <svg class="wave" viewBox="0 0 496 396" aria-hidden="true">
    <path d="M0 292 C 40 280, 62 302, 100 300 S 160 282, 200 290 S 270 306, 312 296 S 380 280, 420 292 S 470 298, 496 286 L496 396 L0 396 Z" fill="var(--conch-pink)"/>
    <path d="M0 292 C 40 280, 62 302, 100 300 S 160 282, 200 290 S 270 306, 312 296 S 380 280, 420 292 S 470 298, 496 286" fill="none" stroke="var(--white)" stroke-width="2"/>
  </svg>
  <div class="conch-art" role="img" aria-label="Line illustration of a pink conch shell"></div>
  <div class="volume">1.5 Liter</div>
  <div class="brand-name">coralis</div>
  <div class="product-name">FILTERED WATER</div>
  <div class="product-note">MINERALS ADDED</div>
  <svg class="recycle-icon" viewBox="0 0 34 34" aria-label="Recyclable">
    <g fill="none" stroke="var(--white)" stroke-width="3.4" stroke-linejoin="round">
      <path d="M11 10 L15 4 L20 4 L24 11"/>
      <path d="M27 17 L30 23 L27 28 L19 28"/>
      <path d="M13 28 L6 28 L3 23 L7 16"/>
    </g>
    <g fill="var(--white)">
      <path d="M21 8 L28 9 L25 15 Z"/>
      <path d="M21 24 L17 28 L21 32 Z"/>
      <path d="M3 15 L11 15 L7 21 Z"/>
    </g>
  </svg>
  <div class="nutrition">
    <div class="nutrition__title">Nutrition<br>Facts</div>
    <div class="nutrition__serving">6.25 servings<br>per container<br>Serving size<br>8 fl oz. (240ml)</div>
    <div class="nutrition__calories">Calories<br>per serving<b>0</b></div>
    <div class="nutrition__col nutrition__col--a">
      <div class="nutrition__row nutrition__row--head"><span>Amount/serving</span><span>%DV</span></div>
      <div class="nutrition__row"><span>Total Fat 0g</span><span>0%</span></div>
      <div class="nutrition__row"><span>Sat. Fat 0g</span><span>0%</span></div>
      <div class="nutrition__row nutrition__row--plain"><span>Trans Fat 0g</span><span></span></div>
      <div class="nutrition__row"><span>Cholestorol 0mg</span><span>0%</span></div>
      <div class="nutrition__row"><span>Sodium 10mg</span><span>1%</span></div>
    </div>
    <div class="nutrition__col nutrition__col--b">
      <div class="nutrition__row nutrition__row--head"><span>Amount/serving</span><span>%DV</span></div>
      <div class="nutrition__row"><span>Total Carb. 0g</span><span>0%</span></div>
      <div class="nutrition__row"><span>Fiber 0g</span><span>0%</span></div>
      <div class="nutrition__row nutrition__row--plain"><span>Total Sugar 0g</span><span></span></div>
      <div class="nutrition__row"><span>Ind. 0g Added Sugar</span><span>0%</span></div>
      <div class="nutrition__row"><span>Protein 0g</span><span>1%</span></div>
    </div>
    <div class="nutrition__foot">*Vitamin D 0% *Calcium 0% *Iron 0% * Potassium 0%</div>
  </div>
  <div class="bottler">
    <p><b>Bottled by:</b><br>Kr Ltd. t/a Coralis Water<br>&amp; Tide Water<br>PO BOX KR 10234</p>
    <p>For more information call<br><b>Sales:</b> 555-014-2<br><b>Office:</b> 555-019-7</p>
  </div>
</div>

<div class="label label--wrapped">
  <div class="brand-band"></div>
  <div class="landscape" role="img" aria-label="Photograph of misty green hills around a calm island lagoon"></div>
  <svg class="wave" viewBox="0 0 496 396" aria-hidden="true">
    <path d="M0 292 C 40 280, 62 302, 100 300 S 160 282, 200 290 S 270 306, 312 296 S 380 280, 420 292 S 470 298, 496 286 L496 396 L0 396 Z" fill="var(--conch-pink)"/>
    <path d="M0 292 C 40 280, 62 302, 100 300 S 160 282, 200 290 S 270 306, 312 296 S 380 280, 420 292 S 470 298, 496 286" fill="none" stroke="var(--white)" stroke-width="2"/>
  </svg>
  <div class="conch-art" role="img" aria-label="Line illustration of a pink conch shell"></div>
  <div class="volume">1.5 Liter</div>
  <div class="brand-name">coralis</div>
  <div class="product-name">FILTERED WATER</div>
  <div class="product-note">MINERALS ADDED</div>
  <svg class="recycle-icon" viewBox="0 0 34 34" aria-label="Recyclable">
    <g fill="none" stroke="var(--white)" stroke-width="3.4" stroke-linejoin="round">
      <path d="M11 10 L15 4 L20 4 L24 11"/>
      <path d="M27 17 L30 23 L27 28 L19 28"/>
      <path d="M13 28 L6 28 L3 23 L7 16"/>
    </g>
    <g fill="var(--white)">
      <path d="M21 8 L28 9 L25 15 Z"/>
      <path d="M21 24 L17 28 L21 32 Z"/>
      <path d="M3 15 L11 15 L7 21 Z"/>
    </g>
  </svg>
  <div class="nutrition">
    <div class="nutrition__title">Nutrition<br>Facts</div>
    <div class="nutrition__serving">6.25 servings<br>per container<br>Serving size<br>8 fl oz. (240ml)</div>
    <div class="nutrition__calories">Calories<br>per serving<b>0</b></div>
    <div class="nutrition__col nutrition__col--a">
      <div class="nutrition__row nutrition__row--head"><span>Amount/serving</span><span>%DV</span></div>
      <div class="nutrition__row"><span>Total Fat 0g</span><span>0%</span></div>
      <div class="nutrition__row"><span>Sat. Fat 0g</span><span>0%</span></div>
      <div class="nutrition__row nutrition__row--plain"><span>Trans Fat 0g</span><span></span></div>
      <div class="nutrition__row"><span>Cholestorol 0mg</span><span>0%</span></div>
      <div class="nutrition__row"><span>Sodium 10mg</span><span>1%</span></div>
    </div>
    <div class="nutrition__col nutrition__col--b">
      <div class="nutrition__row nutrition__row--head"><span>Amount/serving</span><span>%DV</span></div>
      <div class="nutrition__row"><span>Total Carb. 0g</span><span>0%</span></div>
      <div class="nutrition__row"><span>Fiber 0g</span><span>0%</span></div>
      <div class="nutrition__row nutrition__row--plain"><span>Total Sugar 0g</span><span></span></div>
      <div class="nutrition__row"><span>Ind. 0g Added Sugar</span><span>0%</span></div>
      <div class="nutrition__row"><span>Protein 0g</span><span>1%</span></div>
    </div>
    <div class="nutrition__foot">*Vitamin D 0% *Calcium 0% *Iron 0% * Potassium 0%</div>
  </div>
  <div class="bottler">
    <p><b>Bottled by:</b><br>Kr Ltd. t/a Coralis Water<br>&amp; Tide Water<br>PO BOX KR 10234</p>
    <p>For more information call<br><b>Sales:</b> 555-014-2<br><b>Office:</b> 555-019-7</p>
  </div>
</div>

</body>
</html>
```